Signage Design Project - Florida Vacation Resort Monument Sign

I need a design for the main identification sign outside of a resort in Florida. This is a sign that will be located at ground level near the entrance to the resort.

Text to include:

"4818" (This is the property address numbers, no street name necessary)

"Coral Haven" (This is the name of the resort)

"Heated Pool" (bullet point)
"Tiki Hut" (bullet point)
"Beach Access" (bullet point)

"Weekly/Monthly Rentals" (text to appear at bottom of sign)

Dimensions: 55.5"wide x 43.5"tall

Some design elements can protrude from the dimensions, as long as they are not too thin. It will ultimately need to be cut out of wood and if a design element is thin and sticks out of the box, it will be likely to break off.

***The artwork must be vectored.***

Please use whatever design elements you'd like in full color. A palm tree might make sense because of the name "Coral Haven", but I don't want to limit your creativity!

The website is here: http://www.coral-haven-example.com

They have a tour your can click on at the bottom for more pictures to get a feel for the property.

```html
<!DOCTYPE html>
<html lang="en">
<head>
<meta charset="utf-8">
<title>Coral Haven Monument Sign</title>
<link rel="stylesheet" href="https://fonts.googleapis.com/css2?family=Great+Vibes&family=Open+Sans:wght@400&family=Archivo+Black&display=swap">
<style>
  :root {
    --page-bg: #f2f2f2;
    --sky-top: #2ab2d6;
    --sky-mid: #1f86c8;
    --sky-low: #1c6bb4;
    --sea-light: #27a8d8;
    --wave-deep: #1a56a6;
    --sand-orange: #f4a11f;
    --sand-yellow: #f8e52a;
    --hill-brown: #3a1614;
    --accent-orange: #f47f20;
    --number-yellow: #f9ea3a;
    --number-orange: #f47d22;
    --number-shade: #8a8a8a;
    --text-white: #ffffff;
  }
  html, body {
    margin: 0;
    width: 1200px;
    height: 1095px;
    overflow: hidden;
    background: var(--page-bg);
  }
  .monument-sign {
    position: absolute;
    left: 40px;
    top: 141px;
    width: 1120px;
    height: 812px;
    display: block;
  }
  .resort-name {
    font-family: "Great Vibes", cursive;
    font-size: 138px;
    fill: var(--text-white);
  }
  .amenity {
    font-family: "Open Sans", sans-serif;
    font-size: 52px;
    fill: var(--text-white);
  }
  .rental-note {
    font-family: "Open Sans", sans-serif;
    font-size: 40px;
    fill: var(--text-white);
  }
  .address-number {
    font-family: "Archivo Black", sans-serif;
    font-size: 92px;
    letter-spacing: -2px;
  }
  .address-number--shade { fill: var(--number-shade); }
  .address-number--face { fill: url(#numberGradient); }
</style>
</head>
<body>
<svg class="monument-sign" viewBox="0 0 965 700" role="group" aria-label="Coral Haven resort sign">
  <defs>
    <linearGradient id="skyGradient" x1="0" y1="0" x2="0" y2="1">
      <stop offset="0" stop-color="var(--sky-top)"/>
      <stop offset="0.55" stop-color="var(--sky-mid)"/>
      <stop offset="1" stop-color="var(--sky-low)"/>
    </linearGradient>
    <linearGradient id="sandGradient" x1="0" y1="0" x2="1" y2="0">
      <stop offset="0" stop-color="var(--sand-orange)"/>
      <stop offset="0.6" stop-color="var(--sand-yellow)"/>
    </linearGradient>
    <linearGradient id="numberGradient" x1="0" y1="0" x2="1" y2="0">
      <stop offset="0" stop-color="var(--number-yellow)"/>
      <stop offset="1" stop-color="var(--number-orange)"/>
    </linearGradient>
    <radialGradient id="sceneGradient" cx="0.6" cy="0.5" r="0.55">
      <stop offset="0" stop-color="#fbb117"/>
      <stop offset="0.6" stop-color="#e08a1c"/>
      <stop offset="1" stop-color="#4a2418"/>
    </radialGradient>
    <filter id="titleShadow" x="-5%" y="-20%" width="110%" height="140%">
      <feDropShadow dx="3" dy="4" stdDeviation="3" flood-color="#0a3d5c" flood-opacity="0.5"/>
    </filter>
  </defs>

  <!-- sign panel -->
  <rect class="sign-panel" x="0" y="0" width="965" height="700" fill="url(#skyGradient)"/>

  <!-- lower right sea band -->
  <path class="sea-band" d="M520,600 C700,606 850,590 965,570 L965,700 L760,700 Z" fill="var(--sea-light)"/>
  <path class="accent-line-blue" d="M520,600 C700,606 850,585 965,545" fill="none" stroke="var(--wave-deep)" stroke-width="3"/>
  <path class="accent-line-orange" d="M520,594 C700,598 850,575 965,537" fill="none" stroke="var(--accent-orange)" stroke-width="8"/>

  <!-- left waves and hills -->
  <path class="deep-wave" d="M0,425 C120,465 230,510 320,590 L0,590 Z" fill="var(--wave-deep)"/>
  <path class="sand-hill" d="M0,548 C150,520 380,530 570,612 L570,700 L0,700 Z" fill="url(#sandGradient)"/>
  <path class="brown-hill" d="M18,700 C110,620 280,578 420,578 C560,580 680,640 760,700 Z" fill="var(--hill-brown)"/>

  <!-- palm and sun artwork area -->
  <rect class="palm-sunset-art" x="80" y="195" width="335" height="400" rx="30" fill="url(#sceneGradient)" opacity="0.9"
        role="img" aria-label="Two palm tree silhouettes in front of a setting sun"/>

  <!-- resort name -->
  <text class="resort-name" x="100" y="170" textLength="790" lengthAdjust="spacingAndGlyphs" filter="url(#titleShadow)">Coral Haven</text>

  <!-- amenities -->
  <text class="amenity" x="518" y="287">Heated Pool</text>
  <text class="amenity" x="518" y="344">Tiki Hut</text>
  <text class="amenity" x="518" y="403">Beach Access</text>

  <!-- rentals -->
  <text class="rental-note" x="518" y="490">Weekly / Monthly</text>
  <text class="rental-note" x="518" y="540">Rentals Available</text>

  <!-- address number -->
  <text class="address-number address-number--shade" x="220" y="683" aria-hidden="true">4818</text>
  <text class="address-number address-number--face" x="214" y="678">4818</text>
</svg>
</body>
</html>
```